Restyle corporate identity (+ logo) for a road construction company

We need a new logo and stationary design for our company VELMOR path. VELMOR path® increases the road base strength, while reducing major costs and time of road construction. Attached some examples of the current design.

Our wishes for the new logo:
- Business look
- Style sheet
- Modern

More information: www.velmorpath-example.com
Updates

Target Market(s)

Government

Industry/Entity Type

Construction

Requirements
Must have
• Logo (with road sign) + text

```html
<!DOCTYPE html>
<html lang="en">
<head>
<meta charset="utf-8">
<title>VELMOR path — Business Card</title>
<link rel="stylesheet" href="https://fonts.googleapis.com/css2?family=Open+Sans:wght@400;600&display=swap">
<style>
  :root {
    --page-bg: #8e8f8f;
    --card-bg: #e9eaec;
    --brand-blue: #1a7fe0;
    --text-grey: #4d4d4f;
    --muted-grey: #8a8a8c;
    --rule-grey: #b9babc;
  }
  html, body {
    margin: 0;
    padding: 0;
    width: 1105px;
    height: 1200px;
    overflow: hidden;
    background: var(--page-bg);
    font-family: "Open Sans", Arial, sans-serif;
  }
  .canvas {
    position: relative;
    width: 1105px;
    height: 1200px;
  }
  .card {
    position: absolute;
    left: 182px;
    width: 746px;
    height: 427px;
    background: var(--card-bg);
    overflow: hidden;
  }
  .card--front { top: 119px; }
  .card--back { top: 635px; }

  .wordmark {
    position: absolute;
    display: flex;
    align-items: center;
    gap: 10px;
    color: var(--brand-blue);
    font-weight: 600;
    line-height: 1;
    white-space: nowrap;
  }
  .wordmark__square {
    background: var(--brand-blue);
    flex: none;
  }
  .card--front .wordmark {
    left: 76px;
    width: 290px;
    top: 194px;
    font-size: 34px;
  }
  .card--front .wordmark__square { width: 24px; height: 24px; }
  .card--back .wordmark {
    left: 0;
    right: 0;
    justify-content: center;
    top: 192px;
    font-size: 44px;
    gap: 12px;
  }
  .card--back .wordmark__square { width: 30px; height: 30px; }

  .divider {
    position: absolute;
    left: 395px;
    top: 91px;
    width: 1px;
    height: 243px;
    background: var(--rule-grey);
  }

  .contact {
    position: absolute;
    left: 427px;
    top: 88px;
    color: var(--text-grey);
    font-size: 18px;
    line-height: 27px;
  }
  .contact__name {
    color: var(--brand-blue);
    font-weight: 600;
    font-size: 25px;
    line-height: 32px;
  }
  .contact__role {
    color: var(--muted-grey);
    margin-bottom: 14px;
  }
  .contact__address { margin-bottom: 10px; }
  .contact__line {
    display: flex;
    align-items: center;
    gap: 10px;
  }
  .contact__icon { width: 16px; height: 16px; fill: var(--brand-blue); flex: none; }

  .band-rule {
    position: absolute;
    left: 0; right: 0;
    bottom: 32px;
    height: 3px;
    background: var(--rule-grey);
  }
  .band {
    position: absolute;
    left: 0; right: 0;
    bottom: 0;
    height: 29px;
    background: var(--brand-blue);
  }

  .back-url {
    position: absolute;
    left: 0; right: 0;
    top: 358px;
    text-align: center;
    color: var(--text-grey);
    font-size: 20px;
    letter-spacing: 4px;
  }
</style>
</head>
<body>
<main class="canvas">
  <section class="card card--front">
    <div class="wordmark"><span class="wordmark__square"></span>VELMOR path</div>
    <div class="divider"></div>
    <div class="contact">
      <div class="contact__name">Aaron Delvecq</div>
      <div class="contact__role">CEO/Founder</div>
      <div class="contact__address">Lindenkade 58<br>3011 BK Harbourton<br>The Netherlands</div>
      <div class="contact__line">
        <svg class="contact__icon" viewBox="0 0 16 16" aria-hidden="true"><path d="M3.2 1l2.6 2.6-1.5 2a9 9 0 0 0 6.1 6.1l2-1.5L15 12.8 13.2 15C6.5 15 1 9.5 1 2.8z"/></svg>
        <span>612 480 3917</span>
      </div>
      <div class="contact__line">
        <svg class="contact__icon" viewBox="0 0 16 16" aria-hidden="true"><path d="M1 3h14v10H1z M1 3l7 6 7-6" fill="none" stroke="#1a7fe0" stroke-width="1.8"/></svg>
        <span>info@velmorpath-example.com</span>
      </div>
      <div class="contact__line">
        <svg class="contact__icon" viewBox="0 0 16 16" aria-hidden="true"><circle cx="8" cy="8" r="7"/><path d="M5 4c2 1 1 3 3 3s1 3 3 2M4 11c1-1 2 0 3 1" fill="none" stroke="#e9eaec" stroke-width="1.3"/></svg>
        <span>www.velmorpath-example.com</span>
      </div>
    </div>
    <div class="band-rule"></div>
    <div class="band"></div>
  </section>

  <section class="card card--back">
    <div class="wordmark"><span class="wordmark__square"></span>VELMOR path</div>
    <div class="back-url">www.velmorpath-example.com</div>
  </section>
</main>
</body>
</html>
```